Q-VIRO STATIONERY
Q-VIRO Stationery
Project: Q-VIRO STATIONERY
Q-VIRO STATIONERY - Construction
Creative Brief
Simple
KL MARLOW
5172 HOLLOWAY LANE ASHFORD RIDGE GEORGA 309901
Kl@q-viroco.example

```html
<!DOCTYPE html>
<html lang="en">
<head>
<meta charset="utf-8">
<title>Q-VIRO Stationery</title>
<link rel="stylesheet" href="https://fonts.googleapis.com/css2?family=Open+Sans:wght@400;600;700;800&display=swap">
<style>
  :root {
    --backdrop: #262626;
    --brand-blue: #1d4fd6;
    --brand-blue-deep: #0c2fa6;
    --brand-blue-light: #4d86f2;
    --card-white: #ffffff;
    --text-grey: #8a8f99;
    --text-dark: #4a4f59;
  }
  * { box-sizing: border-box; margin: 0; padding: 0; }
  html, body { width: 1200px; height: 751px; overflow: hidden; }
  body {
    background: var(--backdrop);
    font-family: "Open Sans", Arial, sans-serif;
    position: relative;
  }
  .card {
    position: absolute;
    width: 500px;
    height: 286px;
    border-radius: 14px;
    overflow: hidden;
    top: 232px;
  }
  .card-front {
    left: 70px;
    background: linear-gradient(135deg, var(--brand-blue-light) 0%, var(--brand-blue) 45%, var(--brand-blue-deep) 100%);
  }
  .front-mark {
    position: absolute;
    left: 38px;
    top: 48px;
    width: 190px;
    height: 190px;
    border-radius: 50%;
    background: var(--card-white);
  }
  .front-name {
    position: absolute;
    left: 262px;
    top: 104px;
    font-size: 46px;
    font-weight: 800;
    color: var(--card-white);
    letter-spacing: 1px;
  }
  .front-web {
    position: absolute;
    left: 266px;
    top: 164px;
    font-size: 13px;
    color: var(--card-white);
    letter-spacing: 2px;
  }
  .card-back {
    left: 630px;
    background: var(--card-white);
  }
  .back-logo {
    position: absolute;
    left: 120px;
    top: 38px;
    display: flex;
    align-items: center;
    gap: 10px;
  }
  .back-logo-dot {
    width: 40px; height: 40px; border-radius: 50%;
    background: var(--brand-blue);
  }
  .back-logo-name {
    font-size: 34px; font-weight: 800; color: var(--brand-blue);
    letter-spacing: 1px;
  }
  .holder {
    position: absolute;
    left: 54px;
    top: 124px;
  }
  .holder-name {
    font-size: 18px; font-weight: 700; color: var(--brand-blue);
    margin-bottom: 4px;
  }
  .holder-address {
    font-size: 12px; line-height: 17px; color: var(--text-grey);
  }
  .contacts {
    position: absolute;
    left: 292px;
    top: 112px;
    list-style: none;
  }
  .contacts li {
    display: flex; align-items: center; gap: 8px;
    font-size: 12px; color: var(--text-dark);
    height: 22px;
  }
  .contacts svg { width: 13px; height: 13px; fill: var(--brand-blue); }
  .back-band {
    position: absolute;
    left: 0; right: 0; bottom: 0;
    height: 52px;
    background: linear-gradient(90deg, var(--brand-blue-deep), var(--brand-blue) 50%, var(--brand-blue-deep));
    border-top: 4px solid var(--brand-blue-light);
    display: flex; align-items: center; justify-content: center;
  }
  .back-web {
    font-size: 13px; color: var(--card-white); letter-spacing: 3px;
  }
</style>
</head>
<body>
  <section class="card card-front">
    <div class="front-mark"></div>
    <div class="front-name">Q-VIRO</div>
    <div class="front-web">www.q-viroco.example</div>
  </section>

  <section class="card card-back">
    <div class="back-logo">
      <div class="back-logo-dot"></div>
      <div class="back-logo-name">Q-VIRO</div>
    </div>
    <div class="holder">
      <div class="holder-name">KL MARLOW</div>
      <div class="holder-address">5172 Holloway Lane<br>ashford ridge georga 309901</div>
    </div>
    <ul class="contacts">
      <li>
        <svg viewBox="0 0 24 24"><path d="M6.6 10.8a15.1 15.1 0 0 0 6.6 6.6l2.2-2.2c.3-.3.7-.4 1-.2 1.1.4 2.3.6 3.6.6.6 0 1 .4 1 1V20c0 .6-.4 1-1 1A17 17 0 0 1 3 4c0-.6.4-1 1-1h3.5c.6 0 1 .4 1 1 0 1.3.2 2.5.6 3.6.1.3 0 .7-.2 1z"/></svg>
        404-555-0172
      </li>
      <li>
        <svg viewBox="0 0 24 24"><rect x="6" y="2" width="12" height="20" rx="2"/></svg>
        404-555-0190
      </li>
      <li>
        <svg viewBox="0 0 24 24"><path d="M2 5h20v14H2z M2 5l10 8 10-8" /></svg>
        Kl@q-viroco.example
      </li>
    </ul>
    <div class="back-band">
      <span class="back-web">www.q-viroco.example</span>
    </div>
  </section>
</body>
</html>
```